Looking for Desginers for an abstract art canvas & poster stallcraft shop

I want to get a design done for an abstract canvas art & print shop. If possible im looking to create the design based on the harbor or quarry template (im open to suggestions). Mostly I need the creative assets such as banners, images, copywriting, typography etc since im having a hard time to give it a descent look myself.

Target Market(s)

Home decor lovers, abstract art enthusiasts and canvas art enthusiast

Industry/Entity Type

Art

Coding

Coded - Design and coding required

Number of Pages Required

1 page

Colors

Designer to choose only greyscale colors for use in the design.

Requirements
Must have
• Creatives Assets such as banners, images, copy, collection image templates. Please use the velunor logo provided below in at least one of the proposals.
Should not have
• anything that has to be coded into html or css.

```html
<!DOCTYPE html>
<html lang="en">
<head>
<meta charset="utf-8">
<title>Velunor — Abstract Canvas Art &amp; Print Shop</title>
<link href="https://fonts.googleapis.com/css2?family=Playfair+Display:ital,wght@0,400;0,500;0,600;0,700;1,400;1,500&display=swap" rel="stylesheet">
<style>
:root{
  --ink:#2b2b2b;
  --muted:#8a8a8a;
  --accent:#6f6f6f;
  --accent-dark:#5a5a5a;
  --topbar:#111111;
  --hero:#c2c2c2;
  --footer:#1f1f1f;
  --white:#ffffff;
  --img-frame:#d6d6d6;
  --pay:#e6e6e6;
}
*{box-sizing:border-box;margin:0;padding:0}
html,body{width:1200px;height:2642px;overflow:hidden}
body{position:relative;background:var(--white);font-family:'Playfair Display',serif;color:var(--ink)}
.abs{position:absolute}
.topbar{left:0;top:0;width:1200px;height:36px;background:var(--topbar);color:var(--white);font-size:12px}
.topbar .ship{left:142px;top:11px}
.topbar .cart{left:834px;top:10px;display:flex;gap:6px;align-items:center}
.topbar .search{left:898px;top:5px;width:157px;height:26px;border-radius:13px;background:var(--white);color:var(--ink);font-size:11px;display:flex;align-items:center;padding-left:10px;gap:8px}
.logo{font-weight:700;letter-spacing:2px;color:var(--ink)}
.header .logo{left:143px;top:56px;font-size:34px}
.nav{top:68px;right:145px;display:flex;gap:38px;font-size:13px;text-transform:uppercase}
.nav a{color:var(--ink);text-decoration:none;padding-bottom:4px}
.nav a.active{border-bottom:2px solid var(--accent)}
.hero{left:144px;top:121px;width:912px;height:395px;background:var(--hero);overflow:hidden}
.hero h1{position:absolute;left:61px;top:74px;font-size:40px;line-height:48px;font-weight:600;color:#2f2f2f}
.btn{display:inline-flex;align-items:center;justify-content:center;border-radius:30px;text-transform:uppercase;font-weight:500}
.btn-solid{background:var(--accent);color:var(--white)}
.btn-line{border:2px solid var(--accent);color:var(--accent);background:var(--white)}
.hero .btn{position:absolute;left:62px;top:255px;width:153px;height:54px;font-size:17px}
.frame{position:absolute;top:68px;width:182px;height:259px;background:var(--white);padding:10px;box-shadow:2px 3px 6px rgba(0,0,0,.25)}
.frame div{width:100%;height:100%}
.dots{left:548px;top:536px;display:flex;gap:28px;align-items:center;color:var(--accent);font-size:14px}
.dots .d{display:flex;gap:8px;align-items:center}
.dot{width:8px;height:8px;border-radius:50%;border:1.5px solid var(--accent)}
.dot.on{width:6px;height:6px;background:var(--accent);border:none}
.section-title{font-size:40px;font-weight:600;color:#2a2a2a}
.card{width:207px;height:305px;background:var(--white);box-shadow:0 1px 5px rgba(0,0,0,.12);text-align:center}
.card .img{position:absolute;left:9px;top:9px;width:189px;height:203px}
.card .sale{position:absolute;right:12px;top:21px;width:38px;height:38px;border-radius:50%;background:var(--accent);color:var(--white);font-family:Arial,sans-serif;font-size:9px;display:flex;align-items:center;justify-content:center}
.card .name{position:absolute;left:0;width:100%;top:235px;font-size:17px;font-weight:500;text-transform:uppercase}
.card .price{position:absolute;left:0;width:100%;top:268px;font-size:14px;color:var(--accent)}
.news{width:420px}
.news h3{font-size:17px;font-weight:500;line-height:26px;text-transform:uppercase}
.news .date{margin-top:14px;font-size:14px;font-style:italic;color:var(--accent)}
.news p{margin-top:16px;font-size:13.5px;line-height:26px;color:var(--muted);white-space:nowrap}
.feature-img{left:145px;top:1847px;width:480px;height:311px;background:var(--img-frame)}
.panel{position:absolute;top:30px;width:135px;height:252px;box-shadow:2px 3px 5px rgba(0,0,0,.35)}
.feature{left:707px;top:1847px;width:360px}
.feature h2{font-size:23px;font-weight:500}
.feature .price{margin-top:22px;font-size:16px;font-style:italic;color:var(--accent)}
.feature p{margin-top:18px;font-size:13.5px;line-height:26px;color:var(--muted);white-space:nowrap}
.feature .actions{margin-top:32px;display:flex;gap:8px}
.feature .btn{width:170px;height:58px;font-size:17px}
.feature .more{margin-top:28px;font-size:14px;font-style:italic;color:var(--accent)}
.footer{left:0;top:2254px;width:1200px;height:388px;background:var(--footer);color:var(--white)}
.footer .logo{position:absolute;left:142px;top:62px;font-size:34px;color:var(--white)}
.footer .about{position:absolute;left:142px;top:130px;font-size:14px;line-height:23px;white-space:nowrap}
.footer h4{font-size:17px;font-weight:500;color:#b5b5b5;text-transform:uppercase}
.footer .col{position:absolute;top:62px}
.footer .links a{display:block;color:var(--white);text-decoration:none;font-size:14px;margin-top:14px}
.social{display:flex;gap:8px;margin-top:18px}
.social span{width:42px;height:42px;border:1px solid var(--white);border-radius:50%;display:flex;align-items:center;justify-content:center}
.social span i{width:10px;height:10px;background:var(--white);border-radius:2px}
.signup{font-size:14px;line-height:22px;margin-top:14px}
.email{margin-top:20px;width:214px;height:45px;border-radius:23px;background:var(--white);display:flex;align-items:center;justify-content:space-between;padding:2px;color:var(--ink);font-size:12px}
.email span{padding-left:17px}
.email .btn{height:41px;width:106px;font-size:13px}
.copy{left:0;width:1200px;top:2536px;text-align:center;font-size:14px;color:var(--white)}
.cards-pay{left:470px;top:2585px;display:flex;gap:17px}
.cards-pay span{width:30px;height:18px;border-radius:2px;background:var(--pay)}
</style>
</head>
<body>
<div class="abs topbar">
  <span class="abs ship">Free shipping on orders over $50</span>
  <span class="abs cart"><svg width="14" height="12" viewBox="0 0 14 12"><path d="M0 1h2.5l2 7h7l1.5-5H4" fill="none" stroke="#fff" stroke-width="1.3"/><circle cx="5.5" cy="10.5" r="1" fill="#fff"/><circle cx="10.5" cy="10.5" r="1" fill="#fff"/></svg>Cart</span>
  <span class="abs search"><svg width="11" height="11" viewBox="0 0 11 11"><circle cx="4.5" cy="4.5" r="3.5" fill="none" stroke="#333" stroke-width="1.4"/><path d="M7 7l3.5 3.5" stroke="#333" stroke-width="1.4"/></svg>Search</span>
</div>

<header class="header">
  <div class="abs logo">VELUNOR</div>
  <nav class="abs nav"><a class="active">Home</a><a>Prints</a><a>Arts</a><a>Contact</a></nav>
</header>

<section class="abs hero">
  <h1>Abstract<br>Canvas art<br>&amp; print shop</h1>
  <a class="btn btn-solid">View all</a>
  <div class="frame" style="left:378px"><div role="img" aria-label="Abstract print: round sun over brush stroke" style="background:linear-gradient(180deg,#ebebeb 0%,#a8a8a8 30%,#ebebeb 55%,#8c8c8c 80%,#ebebeb 100%)"></div></div>
  <div class="frame" style="left:586px"><div role="img" aria-label="Abstract print: wavy lines over solid block" style="background:linear-gradient(180deg,#ececec 0%,#ececec 30%,#c9c9c9 31%,#c9c9c9 100%)"></div></div>
  <div class="frame" style="left:794px"><div role="img" aria-label="Abstract print: sun over horizon" style="background:linear-gradient(180deg,#ebebeb 0%,#a3a3a3 35%,#9b9b9b 60%,#c8c8c8 100%)"></div></div>
</section>

<div class="abs dots"><span>&#8249;</span><span class="d"><i class="dot"></i><i class="dot on"></i></span><span>&#8250;</span></div>

<h2 class="abs section-title" style="left:141px;top:636px">Popular this week</h2>

<div class="abs card" style="left:144px;top:731px"><div class="img" role="img" aria-label="Abstract flowing profile artwork" style="background:linear-gradient(135deg,#0e0e0e 20%,#7a7a7a 45%,#c4c4c4 60%,#8e8e8e 80%,#0e0e0e)"></div><div class="name">Product name</div><div class="price">$56.75</div></div>
<div class="abs card" style="left:379px;top:731px"><div class="img" role="img" aria-label="Bold abstract paint strokes" style="background:linear-gradient(160deg,#d6d6d6,#a6a6a6 45%,#808080 70%,#4e4e4e)"></div><span class="sale">SALE</span><div class="name">Product name</div><div class="price">$56.75</div></div>
<div class="abs card" style="left:614px;top:731px"><div class="img" role="img" aria-label="Line-drawn leaf with abstract shapes" style="background:linear-gradient(160deg,#f0f0f0,#c3c3c3 60%,#f0f0f0)"></div><div class="name">Product name</div><div class="price">$56.75</div></div>
<div class="abs card" style="left:849px;top:731px"><div class="img" role="img" aria-label="Fluid abstract paint pour" style="background:linear-gradient(160deg,#262626,#6a6a6a 45%,#3d3d3d 70%,#a0a0a0)"></div><div class="name">Product name</div><div class="price">$56.75</div></div>

<div class="abs card" style="left:144px;top:1062px"><div class="img" role="img" aria-label="Vivid abstract bloom" style="background:linear-gradient(135deg,#d2d2d2,#7c7c7c 45%,#4f4f4f 70%,#a7a7a7)"></div><div class="name">Product name</div><div class="price">$56.75</div></div>
<div class="abs card" style="left:379px;top:1062px"><div class="img" role="img" aria-label="Line-drawn leaves with abstract shapes" style="background:linear-gradient(160deg,#efefef,#bdbdbd 40%,#767676 75%,#efefef)"></div><span class="sale">SALE</span><div class="name">Product name</div><div class="price">$56.75</div></div>
<div class="abs card" style="left:614px;top:1062px"><div class="img" role="img" aria-label="Colourful painted animal portrait" style="background:linear-gradient(160deg,#6c6c6c,#4a4a4a 45%,#8f8f8f 70%,#3a3a3a)"></div><div class="name">Product name</div><div class="price">$56.75</div></div>
<div class="abs card" style="left:849px;top:1062px"><div class="img" role="img" aria-label="Dark flower silhouette on pale background" style="background:linear-gradient(160deg,#f1f1f1,#dedede 50%,#cfcfcf 75%,#f1f1f1)"></div><div class="name">Product name</div><div class="price">$56.75</div></div>

<h2 class="abs section-title" style="left:141px;top:1454px">News</h2>

<article class="abs news" style="left:143px;top:1560px">
  <h3>Sed ut perspiciatis unde<br>omnis iste natus</h3>
  <div class="date">May 18, 2021</div>
  <p>Lorem ipsum dolor sit amet, consectetur adipiscing elitsed<br>do eiusmod tempor incididunt ut labore et dolore magna<br>alm suspendisse ultrices gravidsus commodo</p>
</article>
<article class="abs news" style="left:603px;top:1560px">
  <h3>Sed ut perspiciatis unde<br>omnis iste natus</h3>
  <div class="date">May 18, 2021</div>
  <p>Lorem ipsum dolor sit amet, consectetur adipiscing elitsed<br>do eiusmod tempor incididunt ut labore et dolore magna<br>alm suspendisse ultrices gravidsus commodo</p>
</article>

<div class="abs feature-img">
  <div class="panel" role="img" aria-label="Night forest triptych panel with moon" style="left:25px;background:linear-gradient(180deg,#d0d0d0 0%,#2f2f2f 25%,#3b3b3b 70%,#8a8a8a 100%)"></div>
  <div class="panel" role="img" aria-label="Triptych panel with feather" style="left:174px;background:linear-gradient(180deg,#d8d8d8 0%,#686868 40%,#7e7e7e 60%,#8d8d8d 100%)"></div>
  <div class="panel" role="img" aria-label="Night forest triptych panel with birds" style="left:324px;background:linear-gradient(180deg,#d0d0d0 0%,#2f2f2f 25%,#3b3b3b 70%,#6e6e6e 100%)"></div>
</div>

<div class="abs feature">
  <h2>Product Name</h2>
  <div class="price">$72.00</div>
  <p>Lorem ipsum dolor sit amet, consectetur adipiscing elit, sed<br>do eiusmod tempor incididunt ut labore et dolore magna<br>aliquis ipsum suspeidasus commodo viverra</p>
  <div class="actions"><a class="btn btn-solid">Add to cart</a><a class="btn btn-line">Buy it now</a></div>
  <div class="more">Full details &nbsp;<span style="font-style:normal;font-size:11px">&gt;&gt;</span></div>
</div>

<footer class="abs footer">
  <div class="logo">VELUNOR</div>
  <p class="about">Lorem ipsum dolor sit amensectetudipiscing<br>elit, sed do eiusmod tempor incididunt ut<br>labore et dolore magna aliqus ipuspendisse<br>ultrices gravidaisus commodo viverra</p>
  <div class="col links" style="left:480px"><h4>Links</h4><a>Search</a><a>About us</a><a>Contact</a></div>
  <div class="col" style="left:629px"><h4>Follow us</h4><div class="social"><span><i></i></span><span><i></i></span><span><i></i></span></div></div>
  <div class="col" style="left:843px"><h4>Newsletter</h4><p class="signup">Sign up for the latest news, offers<br>and styles</p><div class="email"><span>Enter Email</span><a class="btn btn-solid">Subscribe</a></div></div>
</footer>
<div class="abs copy">Copyright © 2021, Velunor.Al Rights reserved &nbsp;| Privacy Policy | &nbsp;Terms and Use</div>
<div class="abs cards-pay"><span></span><span></span><span></span><span></span><span></span><span></span></div>
</body>
</html>
```